Doors for Chiropractic Office

In my chiropractic office I have 6 treatment rooms and 2 massage rooms. The entire office is going through a remodel. The overall color scheme is very earth tones but in order to add some color, the 6 doors to the treatment rooms will all be a separate color (Red, Blue, Yellow, Green etc)
I need to number each room 1,2,3,4,5,6 and the 2 massage rooms. I had the idea of putting a giant number on each door, so I am looking for some graphic ideas for that project.
The rooms are located with 4 on each side of a long hallway with the 2 massage rooms at the end.
The purpose of numbering each door is to direct the patients where to go.
I have uploaded pictures of the hall way. Pardon the dust since we are under construction but hopefully it gives you an idea of the layout. The door colors will change as stated above.

Requirements
Nice to have
• I would like to see someone come up with a design where each number for the doors are created out of vertebrae's.

```html
<!DOCTYPE html>
<html lang="en">
<head>
<meta charset="utf-8">
<title>Treatment Room Door 01 – Ridgeview Chiropractic</title>
<link rel="stylesheet" href="https://fonts.googleapis.com/css2?family=Merriweather:wght@900&family=Nunito+Sans:wght@800&display=swap">
<style>
  :root {
    --brand-blue: #25a9e0;
    --brand-grey: #8a8a8d;
    --panel-white: #ffffff;
    --page-bg: #eef0f2;
    --text-white: #ffffff;
  }
  * { box-sizing: border-box; margin: 0; padding: 0; }
  html, body {
    width: 1200px;
    height: 960px;
    overflow: hidden;
    background: var(--page-bg);
  }
  .canvas {
    position: relative;
    width: 1200px;
    height: 960px;
  }
  .door-panel {
    position: absolute;
    left: 420px;
    top: 30px;
    width: 360px;
    height: 900px;
    background: var(--panel-white);
    overflow: hidden;
  }
  .dot-corner {
    position: absolute;
    left: 0;
    top: 0;
    width: 360px;
    height: 180px;
  }
  .room-number {
    position: absolute;
    left: 115px;
    top: 97px;
    width: 128px;
    height: 128px;
    border: 4px solid var(--brand-blue);
    border-radius: 50%;
    display: flex;
    align-items: center;
    justify-content: center;
    font-family: "Nunito Sans", Arial, sans-serif;
    font-weight: 800;
    font-size: 74px;
    letter-spacing: -2px;
    color: var(--brand-blue);
    line-height: 1;
  }
  .spine-emblem {
    position: absolute;
    left: 62px;
    top: 215px;
    width: 226px;
    height: 390px;
  }
  .wave-base {
    position: absolute;
    left: 0;
    top: 612px;
    width: 360px;
    height: 288px;
  }
  .clinic-name {
    position: absolute;
    left: 0;
    top: 770px;
    width: 360px;
    text-align: center;
    font-family: "Merriweather", Georgia, serif;
    font-weight: 900;
    color: var(--text-white);
    text-transform: uppercase;
    line-height: 1.1;
    white-space: nowrap;
  }
  .clinic-name__first { font-size: 26px; letter-spacing: 0.5px; }
  .clinic-name__second { font-size: 34px; letter-spacing: 0.3px; }
</style>
</head>
<body>
<main class="canvas">
  <section class="door-panel">
    <svg class="dot-corner" viewBox="0 0 360 180" role="img" aria-label="Blue halftone dot pattern fading from the top edge">
      <defs>
        <linearGradient id="dotFade" x1="0" y1="0" x2="0.35" y2="1">
          <stop offset="0" stop-color="#25a9e0" stop-opacity="0.85"/>
          <stop offset="1" stop-color="#25a9e0" stop-opacity="0"/>
        </linearGradient>
      </defs>
      <path d="M0,0 L360,0 L360,62 C240,40 110,70 0,170 Z" fill="url(#dotFade)"/>
    </svg>

    <div class="room-number">01</div>

    <svg class="spine-emblem" viewBox="0 0 226 390" role="img" aria-label="Spine of vertebrae curving through an open blue ring">
      <defs>
        <radialGradient id="spineTone" cx="0.5" cy="0.5" r="0.5">
          <stop offset="0" stop-color="#25a9e0" stop-opacity="0.35"/>
          <stop offset="0.6" stop-color="#8a8a8d" stop-opacity="0.15"/>
          <stop offset="1" stop-color="#8a8a8d" stop-opacity="0"/>
        </radialGradient>
      </defs>
      <ellipse cx="113" cy="195" rx="110" ry="190" fill="url(#spineTone)"/>
    </svg>

    <svg class="wave-base" viewBox="0 0 360 288" preserveAspectRatio="none">
      <path d="M0,0 C120,-4 250,52 360,118 L360,288 L0,288 Z" fill="var(--brand-blue)"/>
      <path d="M0,16 C125,12 250,66 360,130 L360,288 L0,288 Z" fill="var(--panel-white)"/>
      <path d="M0,27 C130,22 252,76 360,140 L360,288 L0,288 Z" fill="var(--brand-grey)"/>
      <path d="M0,46 C145,40 258,108 360,178 L360,288 L0,288 Z" fill="var(--brand-blue)"/>
    </svg>

    <div class="clinic-name">
      <div class="clinic-name__first">Ridgeview</div>
      <div class="clinic-name__second">Chiropractic</div>
    </div>
  </section>
</main>
</body>
</html>
```